Bramble Roofing Website Relaunch

We require a re-launch of our website, We are a longrun roofing company based in New Zealand, we are rapidly expanding and require a more professionally presented website our current website is www.brambleroofing.co.nz we want something modern, masculine and communicates a "strong" "superior" image, we already have a logo which I have attached we use the orange and silver one as you will see on our current website

Industry/Entity Type

It Company

Number of Pages Required

1 page

Colors
f37122
f78f20
000000
1b1b1b
474747
d3d3d3
f5f5f5

Requirements
Must have
• Images of our work
• Email and Mobile Contact Details
• Link to Facebook page
• Who We Are, What We Do
• Certified Trade Craftsman Logo
• Our Logo

```html
<!DOCTYPE html>
<html lang="en">
<head>
<meta charset="utf-8">
<title>Bramble Roofing — Long Run Roofing Specialists</title>
<link href="https://fonts.googleapis.com/css2?family=Roboto:wght@400;500;700&family=Open+Sans:wght@400;600;700&display=swap" rel="stylesheet">
<style>
:root{
  --orange:#f37122;
  --orange-light:#f78f20;
  --rust:#a7421b;
  --black:#000000;
  --ink:#1b1b1b;
  --grey:#474747;
  --silver:#d3d3d3;
  --mist:#f5f5f5;
  --band:#f0f0f0;
  --white:#ffffff;
}
*{box-sizing:border-box;margin:0;padding:0}
html,body{width:1200px;height:3557px;overflow:hidden}
body{font-family:"Open Sans",Arial,sans-serif;color:var(--grey);background:var(--white);position:relative}
.abs{position:absolute}
.heading{position:absolute;left:0;width:1200px;text-align:center;font-family:"Roboto",Arial,sans-serif;font-size:34px;font-weight:500;color:var(--grey)}
.heading b{color:var(--rust);font-weight:700}
.heading .mark{display:block;width:10px;height:14px;margin:10px auto 0;background:var(--orange);border-radius:50% 50% 40% 40%}

/* top bar */
.topbar{left:0;top:0;width:1200px;height:47px;background:#6f6f6f;color:var(--white);font-family:"Roboto",sans-serif;font-size:16px;font-weight:500}
.topbar .phone{left:176px;top:13px;display:flex;gap:12px;align-items:center}
.topbar .request{left:830px;top:13px;display:flex;gap:12px;align-items:center;letter-spacing:.5px}

/* nav */
.nav{left:0;top:47px;width:1200px;height:76px;background:var(--white)}
.nav a{position:absolute;top:34px;font-family:"Roboto",sans-serif;font-size:15px;font-weight:500;color:var(--ink);text-decoration:none}
.nav a.active{color:var(--orange)}
.brand{position:absolute;left:500px;top:0;width:200px;height:76px;display:flex;align-items:center;justify-content:center;gap:10px;font-family:"Roboto",sans-serif;font-weight:700;font-size:22px;color:var(--orange)}
.brand .sq{width:18px;height:18px;background:var(--orange)}

/* hero */
.hero{left:0;top:123px;width:1200px;height:446px;background:linear-gradient(180deg,#7d8585 0%,#2f3b33 40%,#26312a 70%,#3a3f35 100%)}
.hero .caption{position:absolute;left:0;bottom:0;width:100%;height:59px;background:rgba(0,0,0,.55);color:var(--white);text-align:center;font-family:"Roboto",sans-serif;font-size:32px;font-weight:500;line-height:59px;letter-spacing:1px}
.hero .arrow{position:absolute;top:190px;width:36px;height:36px;background:rgba(255,255,255,.85);display:flex;align-items:center;justify-content:center}

/* about */
.about-brand{left:166px;top:680px;width:225px;height:110px;display:flex;align-items:center;justify-content:center;gap:10px;font-family:"Roboto",sans-serif;font-weight:700;font-size:24px;color:var(--orange)}
.about-brand .sq{width:20px;height:20px;background:var(--orange)}
.about-rule{left:398px;top:620px;width:3px;height:226px;background:var(--orange)}
.about h2{position:absolute;left:432px;top:610px;font-family:"Roboto",sans-serif;font-size:36px;font-weight:700;color:var(--rust)}
.about h2 span{color:var(--grey);font-weight:500}
.about .mark{left:436px;top:660px;width:10px;height:14px;background:var(--orange);border-radius:50% 50% 40% 40%}
.about .copy{left:432px;top:690px;width:735px;font-size:12.5px;line-height:19px;color:var(--grey)}
.about .copy p{margin-bottom:12px}

/* services */
.services{left:0;top:882px;width:1200px;height:660px;background:var(--band)}
.services .intro{position:absolute;left:180px;top:140px;width:840px;text-align:center;font-size:15.5px;font-weight:700;line-height:26px;color:var(--ink)}
.services .intro .list{color:var(--orange);margin:8px 0}
.service{position:absolute;top:300px;width:300px;text-align:center}
.service .diamond{width:190px;height:190px;margin:0 auto;position:relative}
.service .diamond::before{content:"";position:absolute;left:35px;top:35px;width:120px;height:120px;background:var(--white);transform:rotate(45deg);box-shadow:0 0 0 9px #e3e3e3}
.service .diamond svg{position:absolute;left:55px;top:55px}
.service h3{font-family:"Roboto",sans-serif;font-size:19px;font-weight:500;color:var(--ink);margin-top:24px}
.service p{font-size:12.5px;line-height:19px;width:250px;margin:12px auto 0;color:var(--grey)}

/* gallery */
.tile{position:absolute}
.tile.feature{background:#3b3d3b;color:var(--white);text-align:center}
.tile.feature h4{margin-top:105px;font-family:"Roboto",sans-serif;font-size:19px;font-weight:500}
.tile.feature p{width:230px;margin:12px auto 0;font-size:12.5px;line-height:18px}

/* team */
.team-band{left:0;top:2206px;width:1200px;height:657px;background:var(--band)}
.member{position:absolute;top:2330px;width:300px;text-align:center}
.member .frame{width:237px;height:237px;margin:0 auto;position:relative}
.member .frame::before{content:"";position:absolute;left:43px;top:43px;width:151px;height:151px;background:var(--white);transform:rotate(45deg);box-shadow:0 0 0 10px #e3e3e3}
.member .photo{position:absolute;left:55px;top:55px;width:127px;height:127px;transform:rotate(45deg);background:linear-gradient(135deg,#8fae7a,#6a6e62)}
.member h3{font-family:"Roboto",sans-serif;font-size:17px;font-weight:700;color:var(--ink);margin-top:30px}
.member p{width:262px;margin:14px auto 0;font-size:12px;line-height:18px}

/* inquiry */
.field{position:absolute;height:32px;border:1px solid var(--silver);background:var(--white);font-size:13px;color:var(--grey);padding:7px 12px}
.field svg{position:absolute;right:9px;top:7px}
.send{left:546px;top:3173px;width:75px;height:34px;background:linear-gradient(180deg,var(--orange-light),var(--orange));color:var(--white);font-family:"Roboto",sans-serif;font-weight:700;font-size:15px;text-align:center;line-height:34px}

/* footer */
.footer{left:0;top:3250px;width:1200px;height:275px;background:linear-gradient(180deg,#2b2d2c,#1b1b1b)}
.footer .panel{position:absolute;left:517px;top:0;width:240px;height:275px;background:rgba(0,0,0,.45)}
.footer h5{position:absolute;font-family:"Roboto",sans-serif;font-size:16px;font-weight:700;color:var(--white)}
.badges{left:161px;top:3328px;width:342px;height:135px;background:var(--white);display:flex;align-items:center;justify-content:space-around;padding:0 14px}
.badges span{width:95px;height:95px;border-radius:50%}
.contact-row{position:absolute;left:541px;display:flex;gap:14px;color:var(--white);font-size:12.5px;line-height:17px}
.footer-brand{left:783px;top:3352px;width:260px;height:80px;display:flex;align-items:center;gap:12px;font-family:"Roboto",sans-serif;font-weight:700;font-size:28px;color:var(--silver)}
.footer-brand .sq{width:24px;height:24px;background:var(--silver)}
.copyright{left:0;top:3525px;width:1200px;height:32px;background:linear-gradient(90deg,#c4561b,var(--orange),#c4561b);color:var(--white);font-size:12.5px;font-weight:600}
.copyright .left{position:absolute;left:161px;top:7px}
.copyright .right{position:absolute;left:920px;top:7px;display:flex;gap:10px;align-items:center}
.copyright .right i{display:block;width:18px;height:18px;border-radius:50%;border:2px solid var(--white)}
</style>
</head>
<body>

<header>
  <div class="abs topbar">
    <div class="abs phone">
      <svg width="18" height="18" viewBox="0 0 24 24" fill="none" stroke="#fff" stroke-width="2"><path d="M5 3h4l2 5-3 2a12 12 0 0 0 6 6l2-3 5 2v4a2 2 0 0 1-2 2A18 18 0 0 1 3 5a2 2 0 0 1 2-2z"/></svg>
      021 555 01842
    </div>
    <div class="abs request">
      <svg width="18" height="20" viewBox="0 0 18 20" fill="none" stroke="#fff" stroke-width="2"><rect x="2" y="1" width="14" height="18"/><path d="M5 7h8M5 11h8M5 15h5"/></svg>
      REQUEST YOUR SERVICE
    </div>
  </div>
  <nav class="abs nav">
    <a class="active" style="left:161px">HOME</a>
    <a style="left:254px">ABOUT US</a>
    <a style="left:372px">SERVICES</a>
    <div class="brand"><span class="sq"></span>Bramble Roofing</div>
    <a style="left:797px">WORK GALLERY</a>
    <a style="left:943px">CONTACT US</a>
  </nav>
</header>

<section class="abs hero" role="img" aria-label="Photo of a large green long run steel clad shed under a grey sky">
  <div class="arrow" style="left:4px"><svg width="12" height="14" viewBox="0 0 12 14"><path d="M9 1 3 7l6 6" stroke="#333" stroke-width="2.5" fill="none"/></svg></div>
  <div class="arrow" style="right:4px"><svg width="12" height="14" viewBox="0 0 12 14"><path d="m3 1 6 6-6 6" stroke="#333" stroke-width="2.5" fill="none"/></svg></div>
  <div class="caption">LONG RUN ROOFING SPECIALISTS</div>
</section>

<section class="about">
  <div class="abs about-brand"><span class="sq"></span>Bramble Roofing</div>
  <div class="abs about-rule"></div>
  <h2>About Bramble <span>Roofing</span></h2>
  <div class="abs mark"></div>
  <div class="abs copy">
    <p>We are a local, family owned and operated company with over 18 years extensive experience in the roofing industry. Roofing not only Waikato and Auckland but surrounding areas also.</p>
    <p>We are committed to providing superior service to our customers regardless of how big or small your project is. Your satisfaction is our guarantee. We take pride in installing quality products. Offering a workmanship guarantee and manufacturers material warranties where applicable.</p>
    <p>In a fast paced advancing industry we are constantly striving to provide the latest, modern quality installation methods available to ensure customer expectations are exceeded, project targets are met and a high quality finished product is delivered every time.</p>
  </div>
</section>

<section class="abs services">
  <h2 class="heading" style="top:55px"><b>We Provide</b> Services To<span class="mark"></span></h2>
  <div class="intro">
    At Bramble Roofing we offer a variety of professional services specializing in Residential, Industrial and Commercial Long Run Roofing Installations.
    <div class="list">New Roofs &amp; Re-roofs • Metal Cladding • Spouting &amp; Metal Fascia • Down Pipes • Alterations • Extensions.</div>
    We offer a no obligation free quotation, inspection and consultation service.Providing un-biased, honest advice whilst determining services required.
  </div>
  <div class="service" style="left:147px">
    <div class="diamond"><svg width="80" height="80" viewBox="0 0 80 80" fill="#111"><path d="M2 44 22 26l20 18v26H2z"/><path d="M38 44 56 26l22 18v26H38z"/><rect x="14" y="54" width="8" height="16" fill="#fff"/><rect x="52" y="54" width="8" height="16" fill="#fff"/></svg></div>
    <h3>RESIDENTIAL</h3>
    <p>Lorem ipsum dolor sit amet, consectetuer adipiscing elit, sed diam nonummy nibh euismod tincidunt utaclisi.</p>
  </div>
  <div class="service" style="left:450px">
    <div class="diamond"><svg width="80" height="80" viewBox="0 0 80 80" fill="#111"><rect x="10" y="18" width="10" height="30"/><path d="M4 70V44l18-10v10l18-10v10l18-10v36z"/><circle cx="20" cy="12" r="6"/><circle cx="30" cy="8" r="5"/></svg></div>
    <h3>INDUSTRIAL</h3>
    <p>Lorem ipsum dolor sit amet, consectetuer adipiscing elit, sed diam nonummy nibh euismod tincidunt utaclisi.</p>
  </div>
  <div class="service" style="left:754px">
    <div class="diamond"><svg width="80" height="80" viewBox="0 0 80 80" fill="#111"><path d="M14 70V24h18V10h16v14h18v46z"/><g fill="#fff"><rect x="20" y="30" width="6" height="6"/><rect x="37" y="30" width="6" height="6"/><rect x="54" y="30" width="6" height="6"/><rect x="20" y="44" width="6" height="6"/><rect x="37" y="44" width="6" height="6"/><rect x="54" y="44" width="6" height="6"/><rect x="36" y="58" width="8" height="12"/></g></svg></div>
    <h3>COMMERCIAL</h3>
    <p>Lorem ipsum dolor sit amet, consectetuer adipiscing elit, sed diam nonummy nibh euismod tincidunt utaclisi.</p>
  </div>
</section>

<section class="gallery">
  <h2 class="heading" style="top:1584px"><b>Work</b> Gallery<span class="mark"></span></h2>
  <div class="tile feature" style="left:161px;top:1684px;width:321px;height:275px">
    <h4>Lorem Ispum Preaxc</h4>
    <p>Lorem ipsum dolor sit amet, consectetuer adipiscing elit, sed diam nonummy nibh euismod tincidunt utaclisi.</p>
  </div>
  <div class="tile" role="img" aria-label="Steel frame of a new industrial building" style="left:491px;top:1684px;width:311px;height:131px;background:linear-gradient(180deg,#8fb0d0,#6b7b70)"></div>
  <div class="tile" role="img" aria-label="Blue long run roof on a shed" style="left:811px;top:1684px;width:226px;height:121px;background:linear-gradient(180deg,#6f9dd4,#4f6580)"></div>
  <div class="tile" role="img" aria-label="House with a new dark roof and lawn" style="left:491px;top:1826px;width:152px;height:133px;background:linear-gradient(180deg,#a9c2da,#5e7a4a)"></div>
  <div class="tile" role="img" aria-label="Open shed roof under construction" style="left:652px;top:1826px;width:150px;height:133px;background:linear-gradient(180deg,#b7b9b6,#5d584f)"></div>
  <div class="tile" role="img" aria-label="Close view of dark corrugated roofing" style="left:811px;top:1815px;width:226px;height:144px;background:linear-gradient(160deg,#5d7fa8,#26394f)"></div>
  <div class="tile" role="img" aria-label="Row of new homes with long run roofs" style="left:161px;top:1969px;width:480px;height:182px;background:linear-gradient(180deg,#9aa6b2,#4f4a3e)"></div>
  <div class="tile" role="img" aria-label="Large house with a grey roof under a cloudy sky" style="left:650px;top:1969px;width:387px;height:182px;background:linear-gradient(180deg,#9ea4aa,#5a5b58)"></div>
</section>

<section>
  <div class="abs team-band"></div>
  <h2 class="heading" style="top:2238px"><b>Our</b> Team<span class="mark"></span></h2>
  <div class="member" style="left:147px">
    <div class="frame"><div class="photo" role="img" aria-label="Portrait of the company founder"></div></div>
    <h3>Rowan “The Boss”</h3>
    <p>Rowan started Bramble Roofing fulfilling his dream of owning his own business after 15+ years in the roofing industry. His focus, integrity and unrivalled level of expertise ensures he remains a leader in the industry, increasingly in demand and a reputable installer of choice.</p>
  </div>
  <div class="member" style="left:450px">
    <div class="frame"><div class="photo" role="img" aria-label="Portrait of a roofing installer" style="background:linear-gradient(135deg,#7fae6a,#5a7c4a)"></div></div>
    <h3>Cody Marsh</h3>
    <p>Cody has been in the industry for 10+ years. Having entered into roofing straight from school. He has expertise in all roofing installations as well as experience in roofing installations in Australia. Cody is proficient in complex, creative finishing and flashing systems.</p>
  </div>
  <div class="member" style="left:754px">
    <div class="frame"><div class="photo" role="img" aria-label="Portrait of the office manager" style="background:linear-gradient(135deg,#b7b1a8,#6c5e52)"></div></div>
    <h3>Valerie Stone</h3>
    <p>Valerie is Rowan's wife and office manager, she works full time off site, with an employment history of 15+ years in the construction, materials handling equipment &amp; project administration sectors. Her spare time is taken up managing Bramble Roofing, facilitating the daily operations, many clerical positions, health &amp; safety &amp; ensuring client enquires are responded too timely.</p>
  </div>
</section>

<section class="inquiry">
  <h2 class="heading" style="top:2902px"><b>Quick</b> Inquiry<span class="mark"></span></h2>
  <div class="field" style="left:221px;top:3010px;width:372px">Name<svg width="16" height="16" viewBox="0 0 16 16" fill="none" stroke="#f37122" stroke-width="1.5"><circle cx="8" cy="5" r="3"/><path d="M2 15c0-4 3-5 6-5s6 1 6 5z"/></svg></div>
  <div class="field" style="left:221px;top:3060px;width:372px">Company<svg width="16" height="16" viewBox="0 0 16 16" fill="none" stroke="#f37122" stroke-width="1.5"><rect x="3" y="1" width="10" height="14"/><path d="M6 4h4M6 7h4M6 10h4"/></svg></div>
  <div class="field" style="left:221px;top:3112px;width:372px">Email<svg width="16" height="16" viewBox="0 0 16 16" fill="none" stroke="#f37122" stroke-width="1.5"><rect x="1" y="3" width="14" height="10"/><path d="m1 3 7 6 7-6"/></svg></div>
  <div class="field" style="left:607px;top:3010px;width:373px">Subject<svg width="16" height="16" viewBox="0 0 16 16" fill="none" stroke="#f37122" stroke-width="1.5"><path d="M2 14 12 4l2 2L4 16H2z"/></svg></div>
  <div class="field" style="left:607px;top:3060px;width:373px;height:90px">Message<svg width="16" height="16" viewBox="0 0 16 16" fill="none" stroke="#f37122" stroke-width="1.5"><path d="M2 14 12 4l2 2L4 16H2z"/></svg></div>
  <div class="abs send">SEND</div>
</section>

<footer>
  <div class="abs footer" role="img" aria-label="Darkened photo of a house with a new roof behind the footer">
    <div class="panel"></div>
  </div>
  <h5 style="left:161px;top:3287px">Our Accreditations</h5>
  <div class="abs badges">
    <span style="background:#b89a4e"></span>
    <span style="background:#2f3a8f"></span>
    <span style="background:#d3d3d3"></span>
  </div>
  <h5 style="left:541px;top:3287px">Contact Details</h5>
  <div class="contact-row" style="top:3322px">
    <svg width="14" height="18" viewBox="0 0 14 18" fill="#f37122"><path d="M7 0a7 7 0 0 0-7 7c0 5 7 11 7 11s7-6 7-11a7 7 0 0 0-7-7zm0 10a3 3 0 1 1 0-6 3 3 0 0 1 0 6z"/></svg>
    <span>16 Lorem ipsum dolor sit<br>amet sed beneit. Street<br>No-123456</span>
  </div>
  <div class="contact-row" style="top:3389px">
    <svg width="14" height="14" viewBox="0 0 24 24" fill="none" stroke="#f37122" stroke-width="2.5"><path d="M5 3h4l2 5-3 2a12 12 0 0 0 6 6l2-3 5 2v4a2 2 0 0 1-2 2A18 18 0 0 1 3 5a2 2 0 0 1 2-2z"/></svg>
    <span>021 555 01842</span>
  </div>
  <div class="contact-row" style="top:3428px">
    <svg width="16" height="13" viewBox="0 0 16 13" fill="none" stroke="#f37122" stroke-width="1.5"><rect x="1" y="1" width="14" height="11"/><path d="m1 1 7 6 7-6"/></svg>
    <span>hello@brambleroofing.co.nz</span>
  </div>
  <div class="abs footer-brand"><span class="sq"></span>Bramble Roofing</div>
  <div class="abs copyright">
    <span class="left">Copyright© 2017 Bramble Roofing.all Rights Reserved.</span>
    <span class="right">Follow Us On <i></i></span>
  </div>
</footer>

</body>
</html>
```